THE TALL COPPER ATLAS OF PORTS

subtitle: AN INTRO TO SEARCH ENGINE OPTIMIZATION
background: white
dimensions: 1562x2500

Target Market(s)

Marketing professionals

Industry/Entity Type

Digital Marketing

Font styles to use
Sans Serif

Colors
ffffff
1b1b1b
3176b5

Requirements
Should not have
• Images or graphics

```html
<!DOCTYPE html>
<html lang="en">
<head>
<meta charset="utf-8">
<title>The Tall Copper Atlas of Ports — Cover</title>
<link rel="stylesheet" href="https://fonts.googleapis.com/css2?family=Bebas+Neue&display=swap">
<style>
  :root {
    --paper: #ffffff;
    --ink: #1b1b1b;
    --blue: #3176b5;
  }
  html, body {
    margin: 0;
    padding: 0;
    width: 1200px;
    height: 1200px;
    overflow: hidden;
    background: var(--paper);
  }
  .cover {
    display: block;
    width: 1200px;
    height: 1200px;
  }
  .cover-text {
    font-family: "Bebas Neue", "Oswald", sans-serif;
  }
  .band-ink { fill: var(--ink); }
  .band-blue { fill: var(--blue); }
  .title-the { fill: var(--blue); font-size: 86px; }
  .title-tall { fill: var(--paper); font-size: 126px; }
  .title-copper {
    fill: var(--paper);
    stroke: var(--blue);
    stroke-width: 3.5px;
    stroke-linejoin: round;
    font-size: 262px;
  }
  .title-atlas { fill: var(--blue); font-size: 256px; }
  .title-ports { fill: var(--ink); font-size: 256px; }
  .subtitle-frame {
    fill: none;
    stroke: var(--ink);
    stroke-width: 3px;
  }
  .subtitle { fill: var(--ink); font-size: 69px; }
</style>
</head>
<body>
<svg class="cover" viewBox="0 0 1200 1200" xmlns="http://www.w3.org/2000/svg" role="img" aria-label="Book cover: The Tall Copper Atlas of Ports — An intro to search engine optimization">
  <rect class="cover-page" x="240" y="0" width="738" height="1200" fill="var(--paper)"/>

  <g class="cover-text">
    <!-- THE -->
    <rect class="band-ink" x="542" y="0" width="140" height="124"/>
    <text class="title-the" x="552" y="114" textLength="120" lengthAdjust="spacingAndGlyphs">THE</text>

    <!-- TALL -->
    <rect class="band-blue" x="448" y="137" width="530" height="107"/>
    <text class="title-tall" x="467" y="234">TALL</text>

    <!-- COPPER -->
    <text class="title-copper" x="336" y="444" textLength="544" lengthAdjust="spacingAndGlyphs">COPPER</text>

    <!-- ATLAS -->
    <rect class="band-ink" x="240" y="462" width="596" height="203"/>
    <text class="title-atlas" x="402" y="650" textLength="416" lengthAdjust="spacingAndGlyphs">ATLAS</text>

    <!-- OF PORTS -->
    <rect class="band-blue" x="333" y="686" width="645" height="205"/>
    <text class="title-ports" x="350" y="876" textLength="560" lengthAdjust="spacingAndGlyphs">OF PORTS</text>

    <!-- Subtitle -->
    <path class="subtitle-frame" d="M440 1202 V924 H780 V1202"/>
    <text class="subtitle" x="610" y="994" text-anchor="middle" textLength="244" lengthAdjust="spacingAndGlyphs">AN INTRO TO</text>
    <text class="subtitle" x="610" y="1058" text-anchor="middle" textLength="322" lengthAdjust="spacingAndGlyphs">SEARCH ENGINE</text>
    <text class="subtitle" x="610" y="1118" text-anchor="middle" textLength="284" lengthAdjust="spacingAndGlyphs">OPTIMIZATION</text>
  </g>
</svg>
</body>
</html>
```